Web Design Project

Psychotherapist in Private Practice
Practice name "The Quiet Harbour"
The population is professional adults seeking life coaching and change consultation
I am including a photo for inspiration ONLY - It includes the theme of light and tree branches. There does not HAVE to be a photograph . An illustration , concept or theme of nature /light / generativity / growth / creativity is acceptable
Clean sharp lines Light colors, minimalist , modern.
There is a separate project for a logo design that will become part of the web design
Here are examples of two logos/websites I like
http://www.brightmeadowcentre.ca/
http://www.openridgeadvisors.ca/

Target Market(s)

Professional adults seeking life coaching

Industry/Entity Type

Life Coaching

Requirements
Should not have
• Although the business name has 'compassion' in it, designs with hearts in it would have to be pretty stylish, subtle, mature and sophisticated to be considered.

```html
<!DOCTYPE html>
<html lang="en">
<head>
<meta charset="utf-8">
<title>The Quiet Harbour – Psychotherapist in Private Practice</title>
<link rel="stylesheet" href="https://fonts.googleapis.com/css2?family=Roboto+Condensed:wght@300;400&family=Open+Sans:ital,wght@0,400;0,600;1,700&display=swap">
<style>
  :root {
    --blue: #2275b9;
    --ink: #2d2d2d;
    --text: #555;
    --muted: #777;
    --page-top: #e4e4e4;
    --page-mid: #f2f2f3;
    --page-low: #e6e6e6;
    --panel: #f3f3f4;
    --white: #ffffff;
    --line: #d6d6d6;
    --footer: #d9d9d9;
  }
  * { box-sizing: border-box; margin: 0; padding: 0; }
  html, body { width: 879px; height: 1200px; overflow: hidden; }
  body {
    position: relative;
    font-family: "Open Sans", Arial, sans-serif;
    color: var(--text);
    background: linear-gradient(to bottom, var(--page-top) 0, var(--page-mid) 140px, var(--page-mid) 928px, var(--page-low) 928px);
  }
  .condensed { font-family: "Roboto Condensed", "Arial Narrow", sans-serif; }

  /* Header */
  .brand { position: absolute; left: 39px; top: 18px; }
  .brand-name { font-family: "Roboto Condensed", sans-serif; font-size: 41px; font-weight: 400; color: var(--blue); line-height: 1; letter-spacing: -0.5px; }
  .brand-tag { font-family: "Roboto Condensed", sans-serif; font-size: 12px; color: var(--ink); letter-spacing: 1.2px; text-align: right; margin-top: 2px; }
  .call { position: absolute; right: 39px; top: 34px; display: flex; align-items: center; gap: 8px; font-family: "Roboto Condensed", sans-serif; font-size: 19px; color: var(--ink); }

  /* Main panel */
  .panel { position: absolute; left: 21px; top: 86px; width: 837px; height: 874px; background: var(--panel); border: 1px solid #d2d2d2; border-radius: 6px; box-shadow: 0 1px 3px rgba(0,0,0,.12); }
  .nav { display: flex; height: 51px; list-style: none; }
  .nav li { display: flex; align-items: center; justify-content: center; font-family: "Roboto Condensed", sans-serif; font-size: 17px; color: #555; border-right: 1px solid #e2e2e2; }
  .nav li:last-child { border-right: none; }
  .nav li.active { color: var(--blue); }

  .stage { position: absolute; left: 17px; top: 52px; width: 803px; height: 647px; background: var(--white); border-radius: 5px 5px 0 0; }
  .hero { position: absolute; left: 9px; top: 9px; }
  .hero-title { position: absolute; left: 0; width: 803px; top: 322px; text-align: center; font-family: "Roboto Condensed", sans-serif; font-size: 25px; color: var(--blue); }
  .hero-text { position: absolute; left: 163px; width: 477px; top: 355px; text-align: center; font-size: 12px; line-height: 19px; color: #d8d8d8; }

  .features { position: absolute; left: 0; top: 434px; width: 803px; }
  .feature { position: absolute; width: 233px; text-align: center; }
  .feature h3 { font-family: "Roboto Condensed", sans-serif; font-weight: 400; font-size: 17px; color: var(--ink); height: 22px; }
  .feature h3.highlight { color: var(--blue); }
  .feature .photo { margin-top: 4px; width: 233px; height: 139px; border: 3px solid var(--white); box-shadow: 0 0 3px rgba(0,0,0,.3); }
  .photo-a { background: linear-gradient(120deg, #6f5a50 0%, #e9e4da 45%, #b7c4d6 80%, #8ea4c8 100%); }
  .photo-b { background: linear-gradient(110deg, #3a3a3a 0%, #d9d9d9 30%, #eeeeee 60%, #6d6d6d 100%); }
  .photo-c { background: linear-gradient(100deg, #4a4a4a 0%, #bdbdbd 35%, #ececec 65%, #9a9a9a 100%); }

  .welcome { position: absolute; left: 18px; top: 702px; width: 803px; text-align: center; }
  .welcome h2 { font-family: "Roboto Condensed", sans-serif; font-weight: 400; font-size: 21px; color: var(--blue); }
  .welcome p { margin-top: 9px; font-size: 11px; line-height: 21px; text-align: justify; text-align-last: center; color: var(--text); }

  /* Columns */
  .columns { position: absolute; left: 38px; top: 978px; width: 803px; height: 170px; }
  .column { position: absolute; width: 245px; text-align: center; }
  .column h2 { font-family: "Roboto Condensed", sans-serif; font-weight: 400; font-size: 21px; color: var(--blue); padding-bottom: 6px; border-bottom: 1px solid var(--line); }
  .column .lead { margin-top: 9px; font-size: 12.5px; line-height: 19px; color: var(--ink); }
  .column .body { margin-top: 8px; font-size: 11px; line-height: 17px; color: var(--muted); }
  .column .more { display: block; margin-top: 6px; font-size: 9.5px; font-style: italic; font-weight: 700; color: var(--blue); text-decoration: none; }

  /* Footer */
  .footer { position: absolute; left: 0; top: 1158px; width: 879px; height: 42px; background: var(--footer); border-top: 1px solid #cfcfcf; display: flex; justify-content: space-between; align-items: center; padding: 0 38px; font-size: 10.5px; color: #444; }
  .footer-nav a { color: #444; text-decoration: none; }
  .footer-nav a.active, .footer a.policy { color: var(--blue); text-decoration: none; }
  .sep { color: #aaa; margin: 0 5px; }
</style>
</head>
<body>

<header>
  <div class="brand">
    <div class="brand-name">The Quiet Harbour</div>
    <div class="brand-tag">Psychotherapist in Private Practice</div>
  </div>
  <div class="call">
    <svg width="24" height="26" viewBox="0 0 24 26" aria-hidden="true">
      <path d="M6 3 L10 9 L7.5 11.5 C9 15 11 17.5 14 19 L16.5 16.5 L21 20.5 L18 24 C10 23 3 15 2.5 6 Z" fill="#2275b9"/>
      <path d="M14 4 A7 7 0 0 1 20 10" stroke="#2275b9" stroke-width="1.6" fill="none"/>
      <path d="M14 8 A3.5 3.5 0 0 1 17 11" stroke="#2275b9" stroke-width="1.6" fill="none"/>
    </svg>
    <span>Call Now : 555-014-2870</span>
  </div>
</header>

<main class="panel">
  <ul class="nav">
    <li class="active" style="width:106px">Home</li>
    <li style="width:122px">About Us</li>
    <li style="width:117px">Services</li>
    <li style="width:99px">News</li>
    <li style="width:107px">Advice</li>
    <li style="width:146px">Appoinments</li>
    <li style="width:138px">Contact Us</li>
  </ul>

  <section class="stage">
    <svg class="hero" width="785" height="430" viewBox="0 0 785 430">
      <defs>
        <linearGradient id="sunset" x1="0" y1="0" x2="0" y2="1">
          <stop offset="0" stop-color="#d9893f"/>
          <stop offset="0.22" stop-color="#f8ec78"/>
          <stop offset="0.45" stop-color="#f0b95e"/>
          <stop offset="0.52" stop-color="#a98a86"/>
          <stop offset="1" stop-color="#4f4655"/>
        </linearGradient>
        <linearGradient id="shade" x1="0" y1="0" x2="0" y2="1">
          <stop offset="0" stop-color="#d8d8d8"/>
          <stop offset="1" stop-color="#ffffff" stop-opacity="0"/>
        </linearGradient>
      </defs>
      <path d="M-9 318 Q392 520 794 318 L794 370 Q392 540 -9 370 Z" fill="url(#shade)"/>
      <g role="img" aria-label="Sunset over the sea framed by dark tree branches">
        <path d="M0 0 H785 V312 Q392 490 0 312 Z" fill="url(#sunset)"/>
      </g>
      <path d="M0 312 Q392 270 785 312 Q392 490 0 312 Z" fill="#1f1f1f" opacity="0.92"/>
      <path d="M-9 318 Q392 520 794 318" stroke="#ffffff" stroke-width="6" fill="none"/>
    </svg>
    <h1 class="hero-title">Psychotherapist in Private Practice</h1>
    <p class="hero-text">Lorem ipsum dolor sit amet, consectetur adipiscing elit. Vivamus at dolor nisl. Vivamus eget erat at ante vehicula convallis. Quisque</p>

    <div class="features">
      <div class="feature" style="left:19px">
        <h3 class="highlight">Lorem ipsum dolor</h3>
        <div class="photo photo-a" role="img" aria-label="Therapist comforting a distressed client"></div>
      </div>
      <div class="feature" style="left:285px">
        <h3>Consectetur adipiscing</h3>
        <div class="photo photo-b" role="img" aria-label="Client on a couch talking with a therapist"></div>
      </div>
      <div class="feature" style="left:551px">
        <h3>Vivamus at dolor</h3>
        <div class="photo photo-c" role="img" aria-label="Client relaxing in an armchair during a session"></div>
      </div>
    </div>

    <svg style="position:absolute;left:0;top:624px" width="803" height="30" viewBox="0 0 803 30" aria-hidden="true">
      <path d="M0 20 Q401 -14 803 20 L803 30 L0 30 Z" fill="#f3f3f4"/>
      <path d="M0 20 Q401 -14 803 20" stroke="#dcdcdc" stroke-width="2" fill="none"/>
    </svg>
  </section>

  <section class="welcome">
    <h2>Welcome to our site !</h2>
    <p>Lorem ipsum dolor sit amet, consectetur adipiscing elit. Vivamus at dolor nisl. Vivamus eget erat at ante vehicula convallis. Quisque interdum aliquet fringilla. Morbi pharetra blandit arcu, eu vehicula quam sollicitudin ac. In eget nisl nisi. Nullam sed purus interdum, varius leo eu, aliquam elit. Phasellus dignissim auctor massa at dignissim. Duis dignissim orci imperdiet ultricies ultrices. In lacus dolor, dapibus vel enim vel, congue feugiat orci. Integer varius eleifend massa, nec pretium turpis aliquam eget. Nunc ac mollis turpis. Integer eu fringilla lacus, in viverra velit. Aenean ornare ornare nunc nec dapibus. Quisque id nibh nec nisi faucibus pharetra eu et nisi. Donec tellus quam, sodales eu augue in, cursus scelerisque risus.</p>
  </section>
</main>

<section class="columns">
  <article class="column" style="left:0">
    <h2>New Articales</h2>
    <p class="lead">Lorem ipsum dolor sit amet, consectetur adipiscing elit. Vivamus pharetra blandit</p>
    <p class="body">Lorem ipsum dolor sit amet, consectetur adipiscing elit. Vivamus at dolor nisl. Vivamus eget erat at ante vehicula convallis.</p>
    <a class="more" href="#">View More...</a>
  </article>
  <article class="column" style="left:279px">
    <h2>Professional Advice</h2>
    <p class="lead">Lorem ipsum dolor sit amet, consectetur adipiscing elit. Vivamus pharetra blandit</p>
    <p class="body">Lorem ipsum dolor sit amet, consectetur adipiscing elit. Vivamus at dolor nisl. Vivamus eget erat at ante vehicula convallis.</p>
    <a class="more" href="#">View More...</a>
  </article>
  <article class="column" style="left:558px">
    <h2>Work &amp; Career</h2>
    <p class="lead">Lorem ipsum dolor sit amet, consectetur adipiscing elit. Vivamus pharetra blandit</p>
    <p class="body">Lorem ipsum dolor sit amet, consectetur adipiscing elit. Vivamus at dolor nisl. Vivamus eget erat at ante vehicula convallis.</p>
    <a class="more" href="#">View More...</a>
  </article>
</section>

<footer class="footer">
  <nav class="footer-nav">
    <a class="active" href="#">Home</a><span class="sep">/</span><a href="#">About Us</a><span class="sep">/</span><a href="#">Services</a><span class="sep">/</span><a href="#">News</a><span class="sep">/</span><a href="#">Advice</a><span class="sep">/</span><a href="#">Appoinments</a><span class="sep">/</span><a href="#">Contact Us</a>
  </nav>
  <div>The Quiet Harbour &nbsp;© 2013<span class="sep">/</span><a class="policy" href="#">Privacy Policy</a></div>
</footer>

</body>
</html>
```